Book and Ebook Cover for my Upcoming Book

About the Book
------------------
I need a book, ebook and if possible audio cover design for my upcoming book - Lanterns & Larkspur. This is my first book and really looking for a great book cover. The book is about my story, living with Mental Health and how to reclaim control of your life.

Quillbarrow
-----------
I am using quillbarrow.com to self-publish my book so in case of any design-related questions you can just search info on their website.

I have an initial theme I am thinking for the design book cover which I have attached. You can use this as a starting point.

Idea for the theme
---------------------
I am thinking about a phoenix to represent rising from the ashes and rebirth. The phoenix motif will be continued throughout the interior pages of the book. I'd like the cover of the book to be minimal, white with gold lettering, and maybe incorporating wings? feel free to play around with the idea and up for suggestions.

If you can think of something along these lines and make it a lot better that would be great.

What I need
---------------
The book is complete and is Trim size is 6.14 x 9.21” (234 x 156mm). I would need-
1. Book Cover
2. Back & Spine Design
3. Source File
4. Ebook Cover
5. Need multiple revisions to get the best possible outcome
6. My name and book title should also on the front cover
7. The book title should be bigger size than the subtitle

If you can give me Audiobook cover, I would love that as well and can pay extra for it if needed.

I love this for the interior phoenix motif:
https://craftbazaarly.com/InkMoth/7720458-Watercolor-Heron-Clipart-Set#fullscreen

The only other actual book cover I found online that remotely relates to what I am looking for is this -
https://www.lookfinder.example/url?sa=i&url=https%3A%2F%2Fpixelmoor.com%2Fvantrell&psig=QxTrPLm3KZ9vBwE2dYcN41HoJuSA&ust=1598415525610000&source=images&cd=vfe&ved=0CAIQjRxqFwoTCPD_toPAtesCFQAAAAAdAAAAABAD

Target Market(s)

Personal Development
Mental health

Requirements
Must have
• 1. Book Cover
2. Back & Spine Design
3. Source File
4. Ebook Cover
Nice to have
• Audiobook cover as I eventually will be releasing the audio version of the book

```html
<!DOCTYPE html>
<html lang="en">
<head>
<meta charset="utf-8">
<title>Lanterns &amp; Larkspur — Book Cover</title>
<link href="https://fonts.googleapis.com/css2?family=Archivo+Black&family=Barlow+Condensed:wght@500;600&family=Montserrat:wght@600&display=swap" rel="stylesheet">
<style>
  :root {
    --paper: #fbf3f1;
    --paper-blush: #f6dedb;
    --maroon: #6a1216;
    --rose: #e0678a;
    --ink: #1d1a1a;
    --band-gold: #f3ea7a;
    --author-ink: #2b1a12;
    --plume-red: #d9473a;
    --plume-orange: #ee9a55;
    --plume-pink: #e9a3b0;
    --plume-gold: #f5d35c;
  }
  * { margin: 0; padding: 0; box-sizing: border-box; }
  html, body { width: 801px; height: 1200px; overflow: hidden; background: var(--paper); }
  .cover {
    position: relative;
    width: 801px;
    height: 1200px;
    overflow: hidden;
    background:
      radial-gradient(ellipse at 75% 20%, rgba(246,222,219,0.7), transparent 60%),
      radial-gradient(ellipse at 85% 85%, rgba(246,222,219,0.6), transparent 55%),
      var(--paper);
  }
  .phoenix-art {
    position: absolute;
    left: 0;
    top: 0;
    width: 540px;
    height: 1200px;
    background:
      radial-gradient(ellipse 220px 330px at 200px 420px, rgba(217,71,58,0.85), transparent 75%),
      radial-gradient(ellipse 200px 360px at 330px 260px, rgba(238,154,85,0.8), transparent 75%),
      radial-gradient(ellipse 170px 300px at 110px 140px, rgba(233,163,176,0.7), transparent 75%),
      radial-gradient(ellipse 160px 320px at 140px 900px, rgba(245,211,92,0.75), transparent 75%),
      radial-gradient(ellipse 200px 200px at 260px 760px, rgba(233,163,176,0.6), transparent 75%);
  }
  .imprint {
    position: absolute;
    right: 36px;
    top: 528px;
    font-family: "Archivo Black", sans-serif;
    font-size: 34px;
    letter-spacing: 0.62em;
    margin-right: -0.62em;
    color: var(--ink);
    line-height: 1;
  }
  .title {
    position: absolute;
    right: 36px;
    top: 590px;
    text-align: right;
    font-family: "Barlow Condensed", sans-serif;
    font-weight: 600;
    font-size: 114px;
    line-height: 95px;
    color: var(--maroon);
    text-transform: uppercase;
  }
  .subtitle {
    position: absolute;
    right: 36px;
    top: 836px;
    text-align: right;
    font-family: "Barlow Condensed", sans-serif;
    font-weight: 500;
    font-size: 46px;
    line-height: 52px;
    color: var(--rose);
    text-transform: uppercase;
  }
  .author-band {
    position: absolute;
    left: 0;
    top: 1105px;
    width: 801px;
    height: 60px;
    background: linear-gradient(90deg, rgba(243,234,122,0.55) 0%, var(--band-gold) 20%, var(--band-gold) 80%, rgba(243,234,122,0.4) 100%);
    display: flex;
    align-items: center;
    justify-content: center;
  }
  .author {
    font-family: "Montserrat", sans-serif;
    font-weight: 600;
    font-size: 38px;
    color: var(--author-ink);
    text-transform: uppercase;
    letter-spacing: 0.01em;
    margin-left: 2px;
  }
</style>
</head>
<body>
  <main class="cover">
    <div class="phoenix-art" role="img" aria-label="Watercolour phoenix in red, orange, pink and gold rising with spread wings and flowing tail feathers"></div>

    <div class="imprint">VESPERA</div>

    <h1 class="title">Lanterns<br>&amp; Larkspur</h1>

    <p class="subtitle">Manage your mental health<br>reinvent your life and ultimately<br>own your story</p>

    <div class="author-band">
      <p class="author">By Selvi RN</p>
    </div>
  </main>
</body>
</html>
```